Flyer für Führungskräfte-Workshops und Coaching
Wir waren von der Zusammenarbeit begeistert. Katrin hat sich von Anfang an intensiv mit dem Inhalt auseinandergesetzt und uns schon beim ersten kreativen Vorschlag überzeugt. Die Detailarbeit bis zum finalen Entwurf lief professionell und zügig. So arbeiten wir am liebsten. Professionell, sympathisch, klar und zuverlässig. Wir gebe eine ganz klare Empfehlung.
Zielgruppe
Firma/Organisation: fornexa - Personal- und Unternehmensberatung
Wir sind eine (zweiköpfige) Personal- und Unternehmensberatung aus der Hamburger Hafencity, die Coachings, Trainings und moderierte Workshops für Fach- und Führungskräfte anbietet.
Zielgruppe:
• Mittelstandsunternehmen
• Geschäftsführer
• Fach- und Führungskräfte
Aufgabenstellung
Ziel des Flyers:
• Kompetenz in den Bereichen Training, Workshop und Coaching vermitteln
• Flyer soll auf Fachmessen eingesetzt werden (Kaltakquise)
• Gesprächsanlässe für den Erstkontakt mit fornexa
Kernbotschaften:
• Weiterentwicklung von Fach- und Führungskräften in Richtung Wirksamkeit
• Zwei Säulen: Haltung und Führungshandwerk
• Firmenindividuelle Konzeption, praxisnah, relevant, abwechslungsreich
• Wertschätzender Umgang, Fokus auf Teilnehmer-Schwerpunkte
Tonalität:
• Professionell + sympathisch + praktisch/pragmatisch/natürlich
Gestaltung:
• Schwerpunkt auf grafische Elemente
• Wenig Text
• Integration von Logo und Grundfarben von fornexa
• Unkonventionelle Gestaltung, Abgrenzung von der Konkurrenz
Themenbeispiele:
• Umgang mit Verschiedenheit
• Konfliktfähigkeit
• Prozessentwicklung/-optimierung
• Führungshandwerk
• Mitarbeiterführung
• Coaching
• Selbstmanagement
• Zeitmanagement
• Schlagfertigkeit
• Unternehmenskultur
Format:
• DIN A4, 1-fach-Faltung, Endformat DIN A5 (Alternativen möglich)
Bildmaterial:
• Aktuell noch nicht vorhanden, Erstellung nach Vorgaben der Designer
Hinweis:
Dieses Briefing ist eine Kurzfassung. Gerne beantworten wir weitergehende Fragen.

```html
<!DOCTYPE html>
<html lang="de">
<head>
<meta charset="utf-8">
<title>fornexa – Praxisbegleitendes Coaching</title>
<link rel="stylesheet" href="https://fonts.googleapis.com/css2?family=Montserrat:wght@400;500;600;700;800;900&display=swap">
<style>
  :root {
    --green: #7ab829;
    --green-dark: #5f9a1c;
    --slate: #6c7a85;
    --slate-dark: #55616b;
    --text: #5b6670;
    --paper: #ffffff;
    --paper-shade: #eef0f1;
    --stage: #e8e9ea;
  }
  * { box-sizing: border-box; margin: 0; padding: 0; }
  html, body { width: 966px; height: 1200px; overflow: hidden; background: var(--stage); }
  body { font-family: "Montserrat", sans-serif; color: var(--text); position: relative; }

  .spread { position: absolute; left: 68px; width: 830px; height: 587px; display: flex; box-shadow: 0 6px 18px rgba(0,0,0,.15); }
  .spread--outer { top: 8px; }
  .spread--inner { top: 605px; }
  .page { position: relative; width: 415px; height: 587px; overflow: hidden; background: linear-gradient(135deg, var(--paper) 40%, var(--paper-shade)); }
  .page__art { position: absolute; inset: 0; width: 415px; height: 587px; }
  .abs { position: absolute; }

  .brand { font-weight: 700; color: var(--slate); letter-spacing: -0.5px; display: flex; align-items: center; gap: 6px; line-height: 1; }
  .brand__dot { width: 10px; height: 10px; border-radius: 50%; background: var(--green); }
  .tagline { font-size: 8px; color: var(--slate); line-height: 1.25; }

  /* back page */
  .company { font-size: 10px; font-weight: 700; color: var(--green); }
  .contact-list { list-style: none; font-size: 9.5px; color: var(--text); }
  .contact-list li { display: flex; align-items: center; gap: 10px; height: 21px; }
  .contact-list .web { color: var(--green); font-weight: 700; }
  .icon { width: 11px; height: 11px; flex: none; }
  .portrait { position: absolute; width: 62px; height: 72px; background: linear-gradient(160deg, #d8d4cf, #6f7479); box-shadow: 4px 4px 0 var(--green); }
  .person-caption { font-size: 9.5px; line-height: 1.2; text-align: center; color: var(--text); }
  .person-caption b { font-weight: 800; display: block; }

  /* front page */
  .values { left: 0; width: 415px; text-align: center; font-size: 7px; font-weight: 700; color: var(--slate-dark); letter-spacing: .2px; }
  .values span { color: var(--green); }
  .title { left: 0; width: 415px; text-align: center; font-weight: 900; line-height: 1.05; }
  .title__main { font-size: 31px; color: var(--slate); display: block; }
  .title__accent { font-size: 31px; color: var(--green); display: block; }
  .quote { left: 0; width: 415px; text-align: center; font-size: 9px; color: var(--text); }
  .pill { left: 102px; width: 210px; height: 24px; border-radius: 12px; background: var(--green); color: #fff; font-weight: 800; font-size: 12px; display: flex; align-items: center; justify-content: center; }

  /* inner left */
  .intro { left: 28px; width: 360px; font-size: 7.3px; line-height: 1.35; color: var(--text); }
  .section-title { left: 28px; font-size: 12px; font-weight: 800; color: var(--green); }
  .benefits { left: 28px; width: 360px; list-style: none; }
  .benefits li, .topics li { display: flex; gap: 10px; font-size: 9.3px; font-weight: 700; color: var(--slate-dark); line-height: 1.25; }
  .benefits li { margin-bottom: 12px; }
  .tick { width: 10px; height: 10px; flex: none; margin-top: 2px; }

  /* inner right */
  .topics-label { left: 36px; font-size: 26px; font-weight: 900; color: #fff; letter-spacing: .5px; line-height: 1; }
  .topics { left: 30px; width: 290px; list-style: none; }
  .topics li { position: relative; padding-bottom: 4px; margin-bottom: 6px; font-size: 8.8px; }
  .topics li::after { content: ""; position: absolute; left: 20px; right: -10px; bottom: 0; height: 1px; background: var(--green); }
  .topics li::before { content: ""; position: absolute; right: -13px; bottom: -2px; width: 5px; height: 5px; border-radius: 50%; background: var(--green); }
</style>
</head>
<body>

<svg width="0" height="0" style="position:absolute">
  <defs>
    <linearGradient id="photoWarm" x1="0" y1="0" x2="1" y2="1"><stop offset="0" stop-color="#e9e6e2"/><stop offset=".5" stop-color="#c4b8ad"/><stop offset="1" stop-color="#6f6760"/></linearGradient>
    <linearGradient id="photoCool" x1="0" y1="0" x2="1" y2="1"><stop offset="0" stop-color="#f1f2f3"/><stop offset=".6" stop-color="#c9cdd1"/><stop offset="1" stop-color="#5a6470"/></linearGradient>
    <linearGradient id="photoCrowd" x1="0" y1="0" x2="1" y2="0"><stop offset="0" stop-color="#b9a597"/><stop offset=".5" stop-color="#6f6a6e"/><stop offset="1" stop-color="#9e8a80"/></linearGradient>
    <clipPath id="backPhotoClip"><path d="M0 0H415V270C300 285 120 255 0 150Z"/></clipPath>
    <symbol id="tick" viewBox="0 0 10 10"><circle cx="5" cy="5" r="5" fill="#7ab829"/><path d="M2.6 5.2 4.3 6.8 7.4 3.5" fill="none" stroke="#fff" stroke-width="1.4"/></symbol>
  </defs>
</svg>

<!-- Outer spread: back page + title page -->
<section class="spread spread--outer">
  <article class="page page--back">
    <svg class="page__art" viewBox="0 0 415 587">
      <path d="M0 0H415V270C300 285 120 255 0 150Z" fill="url(#photoWarm)" role="img" aria-label="Foto: Trainerin präsentiert vor einer Gruppe von Teilnehmern im Seminarraum"/>
      <path d="M140 280C200 200 245 110 275 0" fill="none" stroke="var(--green)" stroke-width="4" clip-path="url(#backPhotoClip)"/>
      <path d="M0 150C120 255 300 285 415 270" fill="none" stroke="var(--green)" stroke-width="9"/>
      <path d="M0 200L105 262L0 330Z" fill="var(--slate)"/>
      <path d="M0 340L100 340L0 430Z" fill="var(--green)"/>
      <rect x="0" y="560" width="230" height="14" fill="var(--green)"/>
      <rect x="230" y="560" width="185" height="8" fill="var(--slate)"/>
    </svg>

    <div class="abs brand" style="left:140px; top:296px; font-size:40px;"><span class="brand__dot"></span>fornexa</div>
    <p class="abs tagline" style="left:150px; top:342px;">Die passenden Menschen<br>finden, entwickeln und halten</p>

    <p class="abs company" style="left:150px; top:392px;">fornexa oHG</p>
    <ul class="abs contact-list" style="left:150px; top:408px;">
      <li><svg class="icon" viewBox="0 0 12 12"><circle cx="6" cy="6" r="6" fill="var(--green)"/><path d="M6 2.5a2.3 2.3 0 0 0-2.3 2.3C3.7 6.6 6 9.5 6 9.5s2.3-2.9 2.3-4.7A2.3 2.3 0 0 0 6 2.5Z" fill="#fff"/></svg>20459 Hamburg</li>
      <li><svg class="icon" viewBox="0 0 12 12"><circle cx="6" cy="6" r="6" fill="var(--green)"/><path d="M4 3.2 5 4.6 4.5 5.3a4 4 0 0 0 2.2 2.2l.7-.5 1.4 1-.6 1C5.6 9 3 6.4 3 3.8Z" fill="#fff"/></svg>+49 (0) 40 555012-310/311</li>
      <li><svg class="icon" viewBox="0 0 12 12"><circle cx="6" cy="6" r="6" fill="var(--green)"/><rect x="3" y="4" width="6" height="4.2" fill="#fff"/><path d="M3 4 6 6.3 9 4" fill="none" stroke="var(--green)" stroke-width=".8"/></svg>info@fornexa.com</li>
      <li><svg class="icon" viewBox="0 0 12 12"><circle cx="6" cy="6" r="6" fill="var(--green)"/><circle cx="6" cy="6" r="3.2" fill="none" stroke="#fff" stroke-width=".8"/><path d="M2.8 6H9.2M6 2.8v6.4" stroke="#fff" stroke-width=".8"/></svg><span class="web">www.fornexa.com</span></li>
    </ul>

    <div class="portrait" style="left:48px; top:448px;" role="img" aria-label="Porträtfoto Berater"></div>
    <p class="abs person-caption" style="left:22px; top:528px; width:120px;"><b>Hafencity</b>Am Sandtorkai 12</p>

    <div class="portrait" style="left:318px; top:372px;" role="img" aria-label="Porträtfoto Berater"></div>
    <p class="abs person-caption" style="left:290px; top:452px; width:120px;"><b>Markus Heller</b>Stefan Lorenz</p>
  </article>

  <article class="page page--front">
    <svg class="page__art" viewBox="0 0 415 587">
      <path d="M0 0H415V195C330 262 180 300 0 300Z" fill="url(#photoCool)" role="img" aria-label="Foto: Trainerin spricht vor Zuhörern an einer weißen Wand"/>
      <path d="M0 300C180 300 330 262 415 195" fill="none" stroke="var(--green)" stroke-width="9"/>
      <rect x="0" y="560" width="200" height="8" fill="var(--slate)"/>
      <rect x="200" y="556" width="215" height="14" fill="var(--green)"/>
    </svg>

    <div class="abs brand" style="left:110px; top:40px; font-size:34px;"><span class="brand__dot"></span>fornexa</div>
    <p class="abs tagline" style="left:128px; top:80px;">Die passenden Menschen<br>finden, entwickeln und halten</p>

    <p class="abs values" style="top:322px;">PROFESSIONELL <span>+</span> SYMPATHISCH <span>+</span> PRAKTISCH/PRAGMATISCH/NATÜRLICH</p>
    <h1 class="abs title" style="top:340px;"><span class="title__main">Praxisbegleitendes</span><span class="title__accent">Coaching</span></h1>
    <p class="abs quote" style="top:424px;">„Wer zusieht, sieht mehr, als wer mitspielt“, Wilhelm Brandt.</p>
    <p class="abs pill" style="top:446px;">www.fornexa.com</p>
  </article>
</section>

<!-- Inner spread: benefits + topics -->
<section class="spread spread--inner">
  <article class="page page--benefits">
    <svg class="page__art" viewBox="0 0 415 587">
      <path d="M0 0H415V40C320 150 150 190 0 190Z" fill="url(#photoCool)" role="img" aria-label="Foto: Team im Gespräch in einem hellen Büro"/>
      <path d="M0 190C150 190 320 150 415 40V70C320 175 150 208 0 208Z" fill="var(--slate)"/>
      <path d="M0 208C150 208 320 175 415 70V95C320 195 150 224 0 224Z" fill="var(--green)"/>
      <rect x="0" y="560" width="230" height="14" fill="var(--green)"/>
      <rect x="230" y="560" width="185" height="8" fill="var(--slate)"/>
    </svg>

    <p class="abs intro" style="top:240px;">Als „Schatten im Hintergrund“ wird der Coachee (Führungskraft/ Mitarbeiter) im gewohnten Arbeitsumfeld während der Ausübung seiner beruflichen Tätigkeit vom Coach begleitet. Anschließend erhält er eine unmittelbare Rückmeldung zu seiner Kommunikations- und Interaktionsweise bei konkreten Situationen im Arbeitsalltag. Ziel des Coachings ist es, über Rückmeldung und Reflexion Einstellungs- und Verhaltensänderungen zu initiieren, um die persönliche Wirksamkeit zu steigern.</p>
    <h2 class="abs section-title" style="top:305px;">Vorteile des praxisbegleitenden Coachings:</h2>
    <ul class="abs benefits" style="top:330px;">
      <li><svg class="tick"><use href="#tick"/></svg>Geringer zusätzlicher Zeitaufwand – Coaching während des Arbeitsalltags.</li>
      <li><svg class="tick"><use href="#tick"/></svg>Direktes Feedback aufgrund unmittelbarer Beobachtungen.</li>
      <li><svg class="tick"><use href="#tick"/></svg>Praktische Tipps, die sich direkt an den Verhaltensmustern des Coachee orientieren.</li>
      <li><svg class="tick"><use href="#tick"/></svg>Das Beobachtungssetting/ der konkrete Tag wird vom Coachee entsprechend des konkreten Coachinganlasses/ -bedarfs nach Möglichkeit selbst gewählt</li>
      <li><svg class="tick"><use href="#tick"/></svg>Der zeitliche Rahmen wird individuell festgelegt und sollte bestmöglich mindestens zwei Arbeitstage umfassen. (1 Tag Begleitung+Feedback, jeweils ½ Tag nach 1 und 3 Monaten)</li>
      <li><svg class="tick"><use href="#tick"/></svg>Optional können Theorieanteile zu Einstellungen, Selbstorganisation und (Kommunikations-) Verhalten vor- oder nachgeschaltet werden.</li>
    </ul>
  </article>

  <article class="page page--topics">
    <svg class="page__art" viewBox="0 0 415 587">
      <path d="M0 0H100C60 40 30 80 0 105Z" fill="var(--green)"/>
      <path d="M20 150C60 90 100 50 130 0H415V130C300 150 150 160 20 150Z" fill="url(#photoCrowd)" role="img" aria-label="Foto: Seminarteilnehmer hören einem Vortragenden zu"/>
      <path d="M100 0H130C100 50 60 90 20 150H0C40 100 70 50 100 0Z" fill="var(--slate)" opacity=".85"/>
      <path d="M22 166H212L180 206L22 213Z" fill="var(--green)"/>
      <path d="M415 200L350 280L415 330Z" fill="var(--slate)"/>
      <path d="M415 345L345 390L415 430Z" fill="var(--green)"/>
      <rect x="0" y="560" width="230" height="8" fill="var(--slate)"/>
      <rect x="230" y="556" width="185" height="14" fill="var(--green)"/>
    </svg>

    <p class="abs topics-label" style="top:176px;">TOPICS</p>
    <ul class="abs topics" style="top:224px;">
      <li><svg class="tick"><use href="#tick"/></svg>Umgang mit Verschiedenheit</li>
      <li><svg class="tick"><use href="#tick"/></svg>Konfliktfähigkeit und lösungsorientiertes Handeln</li>
      <li><svg class="tick"><use href="#tick"/></svg>Workshop Prozessentwicklung/ Prozessoptimierung</li>
      <li><svg class="tick"><use href="#tick"/></svg>Führungshandwerk – die 5 wichtigsten Führungsaufgaben</li>
      <li><svg class="tick"><use href="#tick"/></svg>Mitarbeiterführung heißt Mitarbeiterentwicklung mit Empathie und Konsequenz</li>
      <li><svg class="tick"><use href="#tick"/></svg>Coaching: - entscheiden können und wollen</li>
      <li><svg class="tick"><use href="#tick"/></svg>Vom Mitarbeiter zur Führungskraft</li>
      <li><svg class="tick"><use href="#tick"/></svg>Selbst- statt Zeitmanagement</li>
      <li><svg class="tick"><use href="#tick"/></svg>Entlastung durch Fokus und klare Ziele</li>
      <li><svg class="tick"><use href="#tick"/></svg>Schlagfertigkeitstraining</li>
      <li><svg class="tick"><use href="#tick"/></svg>Unternehmenskultur Vision, Leitbild + Werte leben und einfordern</li>
    </ul>
  </article>
</section>

</body>
</html>
```